Create the ONLY Supplement line for Male Entrepreneurs! (Veltro Prime MD)

I need a label designed for a new supplement brand that I am launching.

There are five products so need a design that I can simply change the wording for each individual product

The brand name is called veltro prime MD. The focus is male entrepreneurial health.

Target audience is men 35 to 55.

Concepts: the healthier you are in body the more money you will make in business.

Concept to copy: I want to make a clean minimalistic label mimicking Dallamore MD (google it and you'll see what I mean)

Target Market(s)

male entrepreneurs 35-55

Industry/Entity Type

Health Supplement

Colors

Designer to choose colors to be used in the design.

Requirements
Must have
• Modern classy design, similar to Dallamore MD.
Nice to have
• Highlight that the supplement is Doctor Approved.
Should not have
• No loud colors. Present it as high class.

```html
<!DOCTYPE html>
<html lang="en">
<head>
<meta charset="utf-8">
<title>Veltro Prime MD – Health Supplement Label</title>
<link rel="stylesheet" href="https://fonts.googleapis.com/css2?family=Lora&family=Arimo:wght@700&display=swap">
<style>
  :root {
    --paper: #f0efea;
    --ink: #1c1c1c;
    --maroon: #5b2a27;
    --stripe: #f1ead8;
    --stripe-deep: #efe4c6;
    --frame: #3a3a3a;
  }
  html, body {
    margin: 0;
    padding: 0;
    overflow: hidden;
    background: #ffffff;
  }
  .label {
    position: relative;
    width: 1200px;
    height: 644px;
    background: var(--paper);
    box-sizing: border-box;
    border: 1.5px solid var(--frame);
    overflow: hidden;
    font-family: "Lora", Georgia, serif;
  }
  .label__stripes {
    position: absolute;
    inset: 0;
    width: 100%;
    height: 100%;
  }
  .brand-name {
    position: absolute;
    left: 66px;
    top: 72px;
    margin: 0;
    font-weight: 400;
    font-size: 71px;
    line-height: 1;
    color: var(--maroon);
    letter-spacing: -0.5px;
  }
  .product-type {
    position: absolute;
    left: 66px;
    top: 258px;
    margin: 0;
    font-weight: 400;
    font-size: 50px;
    line-height: 1;
    color: var(--ink);
  }
  .product-tagline {
    position: absolute;
    left: 67px;
    top: 334px;
    margin: 0;
    font-size: 26px;
    line-height: 1;
    color: var(--ink);
  }
  .divider {
    position: absolute;
    left: 67px;
    top: 442px;
    width: 1060px;
    height: 6px;
    background: var(--maroon);
  }
  .ingredients {
    position: absolute;
    left: 67px;
    top: 470px;
    margin: 0;
    font-size: 24px;
    line-height: 1;
    color: var(--ink);
  }
  .count, .approval {
    position: absolute;
    top: 574px;
    margin: 0;
    font-family: "Arimo", Arial, sans-serif;
    font-weight: 700;
    font-size: 24px;
    line-height: 1;
    color: var(--maroon);
  }
  .count { left: 67px; }
  .approval { right: 68px; }
</style>
</head>
<body>
  <main class="label">
    <svg class="label__stripes" viewBox="0 0 1200 644" aria-hidden="true">
      <polygon points="1130,0 1190,0 580,644 520,644" fill="var(--stripe)" opacity="0.8"/>
      <polygon points="1200,30 1200,70 650,644 612,644" fill="var(--stripe)" opacity="0.8"/>
      <polygon points="1200,120 1200,644 700,644" fill="var(--stripe-deep)" opacity="0.55"/>
      <polygon points="1200,140 1200,190 770,644 720,644" fill="var(--paper)" opacity="0.6"/>
    </svg>

    <h1 class="brand-name">Veltro Prime MD</h1>
    <h2 class="product-type">Health Supplement</h2>
    <p class="product-tagline">for male entrepreneurial health</p>

    <div class="divider"></div>

    <p class="ingredients">Ingredients: DMAE, Omega-3, Evening Primrose Oil</p>

    <p class="count">30 softgel capsules</p>
    <p class="approval">This supplement is Doctor Approved</p>
  </main>
</body>
</html>
```